LineUp Banner for EDM music Festival!

Hello,

i need a lineup banner for an edm festival.

It should looks similar to the lineup banner uploaded here. I also added the background image.

Feel free to add something you think it looks cool.
Background have to be used. I would need after your work is done the psd file, so I can edit the text / names by myself.

Size should be around 2000x3000.

Thank you

Industry/Entity Type

Festival

Requirements
Must have
• Similar to the lineup banner. Feel free to add something you think it looks cool.
• Background have to be used.
Nice to have
• In best case it will be as most similar as the uploaded lineup banner.

```html
<!DOCTYPE html>
<html lang="en">
<head>
<meta charset="utf-8">
<title>AAA Festival — Lineup Poster</title>
<link rel="stylesheet" href="https://fonts.googleapis.com/css2?family=Pathway+Gothic+One&family=Roboto+Condensed:wght@400;700&display=swap">
<style>
  :root {
    --sky-blue: #4a4fc4;
    --sky-violet: #8a3fc0;
    --sky-pink: #b8457e;
    --glow-yellow: #f6e7a0;
    --glow-peach: #e8b37a;
    --crowd-brown: #6a3a22;
    --crowd-dark: #1e1210;
    --gold-light: #fff6e4;
    --gold-mid: #f0b870;
    --gold-deep: #c2661a;
    --white: #ffffff;
    --ink: #111111;
  }
  html, body { margin: 0; padding: 0; overflow: hidden; }
  body { width: 800px; height: 1200px; background: var(--ink); }

  .poster {
    position: relative;
    width: 800px;
    height: 1200px;
    overflow: hidden;
    font-family: "Pathway Gothic One", "Arial Narrow", sans-serif;
    color: var(--white);
  }

  .poster__backdrop {
    position: absolute; inset: 0;
    background:
      radial-gradient(ellipse 45% 8% at 50% 14%, rgba(255,170,110,.6), transparent 75%),
      radial-gradient(ellipse 90% 22% at 45% 60%, rgba(255,240,170,.85), transparent 75%),
      linear-gradient(180deg, rgba(0,0,0,0) 0%, rgba(0,0,0,0) 38%, var(--glow-yellow) 56%, var(--glow-peach) 64%, var(--crowd-brown) 80%, var(--crowd-dark) 100%),
      linear-gradient(100deg, var(--sky-blue) 0%, var(--sky-violet) 45%, var(--sky-pink) 100%);
  }

  .presenter {
    position: absolute; top: 36px; left: 0; right: 0;
    text-align: center;
    font-family: "Roboto Condensed", "Arial Narrow", sans-serif;
    font-size: 26px; letter-spacing: 6px;
    text-shadow: 1px 1px 2px rgba(0,0,0,.7);
  }

  .festival-title {
    position: absolute; top: 92px; left: 0; right: 0;
    margin: 0; text-align: center;
    font-family: "Roboto Condensed", "Arial Narrow", sans-serif;
    font-weight: 700; font-size: 120px; letter-spacing: -2px; line-height: 1;
    transform: scaleX(.9);
    background: linear-gradient(90deg, var(--gold-deep) 0%, var(--gold-light) 35%, var(--gold-mid) 70%, var(--gold-deep) 100%);
    -webkit-background-clip: text; background-clip: text;
    color: transparent;
    filter: drop-shadow(2px 3px 0 rgba(40,10,40,.85));
  }

  .event-date {
    position: absolute; top: 240px; left: 0; right: 0;
    text-align: center;
    font-family: "Roboto Condensed", "Arial Narrow", sans-serif;
    font-weight: 700; font-size: 70px; line-height: 1; letter-spacing: -1px;
    transform: scaleX(.83);
    background: linear-gradient(180deg, var(--gold-light) 30%, var(--gold-mid) 100%);
    -webkit-background-clip: text; background-clip: text;
    color: transparent;
    filter: drop-shadow(2px 3px 0 rgba(40,10,40,.8));
  }

  .lineup {
    position: absolute; top: 370px; left: 36px;
    display: grid; grid-template-columns: 396px 370px;
    margin: 0; padding: 0; list-style: none;
  }
  .lineup__artist {
    font-size: 74px; line-height: 72px; letter-spacing: -1px;
    white-space: nowrap;
    text-shadow: 3px 3px 0 var(--ink);
  }

  .info {
    position: absolute; top: 946px; left: 0; right: 0;
    text-align: center;
    font-size: 31px; line-height: 32px;
    white-space: nowrap;
    text-shadow: 2px 2px 0 var(--ink);
  }
  .info__title { margin: 0 0 4px; font: inherit; }
  .info__line { margin: 0; }

  .sponsors {
    position: absolute; top: 1122px; left: 0; right: 0;
  }
  .sponsors__heading {
    display: flex; align-items: center; gap: 10px;
    font-size: 22px;
    text-shadow: 1px 1px 0 var(--ink);
  }
  .sponsors__heading::before,
  .sponsors__heading::after {
    content: ""; flex: 1; height: 2px; background: var(--white);
  }
  .sponsors__list {
    display: flex; justify-content: center; gap: 10px;
    margin: 10px 0 0; padding: 0; list-style: none;
  }
  .sponsors__item {
    width: 30px; height: 30px; background: var(--white); color: var(--ink);
    display: flex; align-items: center; justify-content: center; text-align: center;
    font-family: "Roboto Condensed", "Arial Narrow", sans-serif;
    font-size: 9px; line-height: 9px;
  }
</style>
</head>
<body>
  <main class="poster">
    <div class="poster__backdrop" role="img" aria-label="Festival crowd with raised hands under purple and golden stage lights"></div>

    <div class="presenter">AAA PRESENT</div>
    <h1 class="festival-title">AAA Festival</h1>
    <div class="event-date">OCTOBER 31,SUNDAY</div>

    <ul class="lineup">
      <li class="lineup__artist">DJ ARTIST NAME</li>
      <li class="lineup__artist">DJ ARTIST NAME</li>
      <li class="lineup__artist">DJ ARTIST NAME</li>
      <li class="lineup__artist">DJ ARTIST NAME</li>
    </ul>

    <section class="info">
      <h2 class="info__title">GENERAL INFORMATIONS</h2>
      <p class="info__line">GENERAL INFORMATIONS • GENERAL INFORMATIONS • GENERAL INFORMATIONS</p>
      <p class="info__line">GENERAL INFORMATIONS • GENERAL INFORMATIONS • GENERAL INFORMATIONS</p>
      <p class="info__line">GENERAL INFORMATIONS • GENERAL INFORMATIONS • GENERAL INFORMATIONS</p>
    </section>

    <footer class="sponsors">
      <div class="sponsors__heading">SPONSORS</div>
      <ul class="sponsors__list">
        <li class="sponsors__item">AAA<br>LOGO</li>
        <li class="sponsors__item">AAA<br>LOGO</li>
        <li class="sponsors__item">AAA<br>LOGO</li>
        <li class="sponsors__item">AAA<br>LOGO</li>
        <li class="sponsors__item">AAA<br>LOGO</li>
        <li class="sponsors__item">AAA<br>LOGO</li>
        <li class="sponsors__item">AAA<br>LOGO</li>
        <li class="sponsors__item">AAA<br>LOGO</li>
      </ul>
    </footer>
  </main>
</body>
</html>
```